Boutique Barre Studio in Geneva

Business card for pilates and dance studio. We are a brand new studio and love our fresh image with our yellow color. This business card is meant for our founder.

```html
<!DOCTYPE html>
<html lang="en">
<head>
<meta charset="utf-8">
<title>Formline Studio – Business Card</title>
<link rel="stylesheet" href="https://fonts.googleapis.com/css2?family=Montserrat:wght@400;600;800&display=swap">
<style>
  :root {
    --canvas: #b3b3b3;
    --card-yellow: #f4ea86;
    --ink: #1b1b1b;
    --photo-light: #dfe5ec;
    --photo-mid: #c6d0da;
    --photo-figure: #3f5a63;
    --photo-floor: #e6ddd2;
  }
  * { box-sizing: border-box; margin: 0; padding: 0; }
  html, body { width: 1200px; height: 846px; overflow: hidden; }
  body {
    background: var(--canvas);
    font-family: "Montserrat", Arial, sans-serif;
    color: var(--ink);
    display: flex;
    align-items: center;
    justify-content: center;
    gap: 40px;
  }
  .card {
    position: relative;
    width: 540px;
    height: 310px;
    border-radius: 28px;
    overflow: hidden;
    box-shadow: 0 10px 24px rgba(0,0,0,0.18);
  }

  /* Front: contact side */
  .card--front { background: var(--card-yellow); }
  .brand-name {
    font-weight: 800;
    font-size: 34px;
    letter-spacing: 0.5px;
    line-height: 1;
  }
  .card--front .brand-name {
    position: absolute;
    left: 150px;
    top: 62px;
  }
  .holder {
    position: absolute;
    left: 70px;
    top: 168px;
  }
  .holder__name { font-weight: 800; font-size: 14px; }
  .holder__role { font-weight: 400; font-size: 13px; margin-top: 4px; }
  .contacts {
    position: absolute;
    left: 270px;
    top: 150px;
    list-style: none;
    font-size: 13px;
  }
  .contacts li { display: flex; align-items: center; gap: 10px; margin-bottom: 8px; }
  .contacts svg { width: 18px; height: 18px; flex: none; }
  .divider {
    position: absolute;
    left: 70px;
    right: 60px;
    top: 222px;
    border-top: 1px solid var(--ink);
  }
  .address {
    position: absolute;
    left: 70px;
    right: 60px;
    top: 234px;
    text-align: center;
    font-size: 13px;
  }

  /* Back: photo side */
  .card--back { background: var(--photo-light); }
  .photo-fill {
    position: absolute;
    inset: 0;
    background:
      linear-gradient(180deg, transparent 62%, var(--photo-floor) 100%),
      radial-gradient(ellipse 60% 40% at 62% 55%, var(--photo-figure) 0%, rgba(63,90,99,0.35) 45%, transparent 75%),
      linear-gradient(135deg, var(--photo-mid), var(--photo-light));
  }
  .card--back .brand-name {
    position: absolute;
    left: 40px;
    top: 110px;
  }
  .website {
    position: absolute;
    right: 40px;
    bottom: 34px;
    font-weight: 600;
    font-size: 15px;
    letter-spacing: 1px;
  }
</style>
</head>
<body>
  <section class="card card--front" aria-label="Business card, contact side">
    <div class="brand-name">Formline Studio</div>
    <div class="holder">
      <p class="holder__name">Mara Delvaux</p>
      <p class="holder__role">Founder</p>
    </div>
    <ul class="contacts">
      <li>
        <svg viewBox="0 0 24 24" fill="none" stroke="currentColor" stroke-width="1.8" stroke-linecap="round" stroke-linejoin="round" aria-hidden="true">
          <path d="M22 16.9v3a2 2 0 0 1-2.2 2 19.8 19.8 0 0 1-8.6-3.1 19.5 19.5 0 0 1-6-6A19.8 19.8 0 0 1 2.1 4.2 2 2 0 0 1 4.1 2h3a2 2 0 0 1 2 1.7c.1.9.4 1.8.7 2.7a2 2 0 0 1-.5 2.1L8 9.8a16 16 0 0 0 6 6l1.3-1.3a2 2 0 0 1 2.1-.4c.9.3 1.8.6 2.7.7a2 2 0 0 1 1.7 2z"/>
        </svg>
        <span>+41 22 555 0148</span>
      </li>
      <li>
        <svg viewBox="0 0 24 24" fill="none" stroke="currentColor" stroke-width="1.8" stroke-linejoin="round" aria-hidden="true">
          <rect x="2.5" y="5" width="19" height="14" rx="1.5"/>
          <path d="M3 6l9 7 9-7"/>
        </svg>
        <span>hello@formline-studio.com</span>
      </li>
    </ul>
    <div class="divider"></div>
    <p class="address">Rue des Lilas 12 / 1205 Geneva / Switzerland</p>
  </section>

  <section class="card card--back" aria-label="Business card, photo side">
    <div class="photo-fill" role="img" aria-label="Photo of a woman in teal sportswear doing a glute bridge on a mat in a bright studio"></div>
    <div class="brand-name">Formline Studio</div>
    <p class="website">WWW.FORMLINE-STUDIO.COM</p>
  </section>
</body>
</html>
```